Broschüre für Immobilienmakler
Tolverik hat unsere Vorstellungen erkannt und von Beginn an super umgesetzt. Natürlich waren noch nachträgliche Änderungen und Feinabstimmungen notwendig. Diese wurden wunschgemäß perfektioniert. Man hatte hier wirklich sehr schöne Ideen in den Details ohne den Blick auf das Ganze zu verlieren. Dadurch haben wir jetzt eine perfekte Broschüre erhalten. Das war bestimmt nicht unser letztes Projekt. Vielen Dank
Zielgruppe
Wir sind Immobilienmakler & Home Stager; unsere hauptsächliche Zielgruppe sind Personen, die Ihre Immobilie verkaufen möchten. Die Broschüre soll ein wichtiger Teil der Akquise werden. Wir vermitteln als Immobilienmakler ganz ursprünglich, jedoch bieten wir auch den gesamten Service rund um den Verkauf (Einholung Unterlagen, Präsentieren der Immobilie durch kleine Effekte bis hin zu Entrümpelungen und Renovierung inkl. Einrichtungsbeispiele/Deko). Zudem sind wir jeden Tag (auch Sonn-und Feiertags) für unsere Kunden erreichbar und auch in Terminen. (Eindrücke gibt es auch über unsere Vexora-Bewertungen)
Aufgabenstellung
Wir möchten einerseits natürlich mit unseren Vorzügen ggü. den 'Standard-Maklern' werben, aber auch genauso professionell den 'Standard-Dienst' ohne Home-Staging anbieten. (Viele Kunden denken schnell, dass wir nur außergewöhnliche und arbeitsintensive Objekte annehmen).
Texte würden wir versuchen zu übernehmen (hier würden wir die vorgesehenen Textfelder der Designer nutzen) und Bilder müssten vermutlich abgesprochen werden, da wir nicht sicher sind, ob unser Material dafür ausreicht. Die Bilder der Homepage liegen hier vor und können gerne zusätzlich gesendet werden.
Unsere Schriftart ist die Museo Sans rounded

```html
<!DOCTYPE html>
<html lang="de">
<head>
<meta charset="utf-8">
<title>Heimwahl – Broschüre Immobilienmakler</title>
<link href="https://fonts.googleapis.com/css2?family=Nunito:wght@300;400;600;700;800&display=swap" rel="stylesheet">
<style>
  :root{
    --stage:#d9d9db;
    --paper:#e6e4e8;
    --paper-white:#ffffff;
    --lilac:#8f7ea3;
    --lilac-light:#a493b6;
    --lilac-text:#7d6b93;
    --ink:#3d3b40;
    --ink-soft:#5b5960;
    --fact-box:rgba(92,88,102,.82);
  }
  *{box-sizing:border-box;margin:0;padding:0}
  html,body{width:1200px;height:800px;overflow:hidden}
  body{background:var(--stage);font-family:"Nunito",sans-serif;color:var(--ink);position:relative}

  .page{position:absolute;top:145px;width:360px;height:510px;overflow:hidden;box-shadow:0 6px 18px rgba(0,0,0,.18)}

  /* ---------- Cover ---------- */
  .cover{left:40px;background:var(--paper)}
  .cover-band{position:absolute;right:0;top:0;width:120px;height:300px;background:var(--lilac)}
  .cover-lines{position:absolute;left:215px;top:40px;width:105px}
  .cover-lines span{display:block;height:3px;background:var(--lilac);margin-bottom:5px}
  .brand{position:absolute;left:28px;top:26px;display:flex;align-items:center;gap:8px}
  .brand-dot{width:30px;height:30px;border-radius:50%;background:var(--lilac)}
  .brand-name{font-weight:800;font-size:15px;letter-spacing:.5px;color:var(--ink);line-height:1}
  .brand-tag{font-size:5.5px;letter-spacing:.6px;color:var(--ink-soft);margin-top:2px}
  .cover-vertical{position:absolute;left:26px;top:345px;transform-origin:0 0;transform:rotate(-90deg);
    font-weight:300;font-size:21px;letter-spacing:1px;color:var(--ink);white-space:nowrap}
  .cover-photo{position:absolute;left:68px;top:95px;width:272px;height:250px;
    background:linear-gradient(135deg,#b8a468 0%,#7f8a4a 45%,#c9b27a 75%,#8e7d55 100%)}
  .cover-headline{position:absolute;left:28px;top:357px;font-size:15px;font-weight:700;color:var(--ink)}
  .cover-headline em{font-style:normal;font-weight:600;color:var(--lilac-text)}
  .cover-band-bottom{position:absolute;left:0;right:0;top:390px;height:82px;background:var(--lilac);
    padding:12px 26px;color:#fff;font-size:9px;line-height:1.55}
  .cover-band-bottom b{font-weight:800}

  /* ---------- Spread ---------- */
  .spread-left{left:440px;background:var(--paper-white)}
  .spread-right{left:800px;background:var(--lilac)}
  .gutter{position:absolute;top:145px;left:780px;width:40px;height:510px;
    background:linear-gradient(90deg,rgba(0,0,0,0),rgba(0,0,0,.12) 50%,rgba(0,0,0,0));pointer-events:none}

  .welcome-band{position:absolute;left:0;top:0;width:100%;height:22px;background:var(--lilac)}
  .welcome-photo{position:absolute;left:28px;top:22px;width:316px;height:190px;border-bottom-right-radius:40px;
    background:linear-gradient(170deg,#a9c4de 0%,#dfe7ef 35%,#4b5a3a 60%,#6f8b45 80%,#c6c3bd 100%)}
  .welcome-title{position:absolute;left:28px;top:222px;font-size:25px;font-weight:700;color:var(--lilac-text)}
  .welcome-sub{position:absolute;left:28px;top:256px;width:310px;font-size:10.5px;color:var(--ink);line-height:1.3}
  .welcome-cols{position:absolute;left:28px;top:292px;width:310px;display:flex;gap:16px;font-size:7.2px;line-height:1.5;color:var(--ink-soft)}
  .welcome-cols .col{flex:1}
  .welcome-cols p{margin-bottom:7px}
  .portrait{float:right;width:58px;height:66px;margin:0 0 4px 6px;border-radius:4px;
    background:linear-gradient(180deg,#9aa0a8,#55585f)}
  .signature{width:110px;height:26px;margin-top:6px;border-radius:3px;background:linear-gradient(90deg,#d9d6dd,#eceaee)}

  .room-photo{position:absolute;left:0;top:28px;width:332px;height:482px;
    background:linear-gradient(180deg,#4a3526 0%,#2d241d 22%,#e9e6e2 40%,#d8d4cf 70%,#eeeeee 100%)}
  .fact-box{position:absolute;left:140px;top:320px;width:192px;height:170px;background:var(--fact-box);
    padding:14px 14px;color:#fff}
  .fact-label{font-size:7.5px;font-weight:700}
  .fact-number{font-size:46px;font-weight:800;color:#cfc6db;line-height:1.05;margin:4px 0 4px}
  .fact-text{font-size:7px;line-height:1.5}
  .fact-source{font-size:5.5px;margin-top:6px;opacity:.85}
</style>
</head>
<body>

<section class="page cover">
  <div class="cover-band"></div>
  <div class="cover-lines"><span></span><span></span><span></span></div>
  <div class="brand">
    <div class="brand-dot"></div>
    <div>
      <div class="brand-name">HEIMWAHL</div>
      <div class="brand-tag">DIE IMMOBILIENMAKLER</div>
    </div>
  </div>
  <div class="cover-photo" role="img" aria-label="Foto: Hand hält ein Modellhaus mit Anhänger „Haus zu verkaufen!“"></div>
  <div class="cover-vertical">DIE IMMOBILIENMAKLER</div>
  <h1 class="cover-headline"><em>Ihr Partner</em> beim Verkauf Ihrer Immobilie</h1>
  <div class="cover-band-bottom">
    <b>Verleihen Sie Ihrer Immobilie den Wow-Effekt!</b> Mit unserem Home-staging-Service verwandeln wir Räume in einladende Oasen. Begeistern Sie potenzielle Käufer und steigern Sie den Verkaufserfolg.
  </div>
</section>

<section class="page spread-left">
  <div class="welcome-band"></div>
  <div class="welcome-photo" role="img" aria-label="Foto: modernes Haus mit Giebel und grünen Sträuchern"></div>
  <h2 class="welcome-title">Herzlich willkommen</h2>
  <p class="welcome-sub">Ihr Immobilienvermittler rund um Verkauf, Home Staging und Beratung</p>
  <div class="welcome-cols">
    <div class="col">
      <p>Ich bin Jonas Berend, Geschäftsführer von Heimwahl und Ihr Partner für optimalen Verkaufserfolg.</p>
      <p>Wir sind nicht nur einen Vermittler, der Ihnen das neue Zuhause zeigt. Mit kreativen Experten verwandeln wir Räume in professionelle Bilder und präsentieren, was Sie verkaufen wollten. Aufgrund dessen finden wir so die passenden Käufer.</p>
      <p>Ihre Zufriedenheit ist unsere höchste Priorität. Nur so erzielen wir Resonanz und einen erfolgreichen Verkauf Ihrer Immobilie. Ein kooperatives Miteinander ist uns wichtig. Sie sollen sich bei uns wohlfühlen und zufrieden sein.</p>
    </div>
    <div class="col">
      <div class="portrait" role="img" aria-label="Porträtfoto des Geschäftsführers"></div>
      <p>Vom „einfachen“ Immobilienverkauf bis hin zu unserem gesamten Angebot des Home Staging – wir versprechen Ihnen immer unsere absolute Professionalität und volles Engagement. Selbstverständlich betreuen wir Sie und Ihre Käufer auch die gesamte Zeit über bis hin zur Übergabe der Immobilie. Lehnen Sie sich zurück und genießen Sie die angenehme Art der Immobilienvermittlung.</p>
      <p>Wir freuen uns auf Sie, Ihre Immobilie und einen angenehmen und erfolgreichen Immobilienverkauf mit Ihnen.</p>
      <div class="signature" role="img" aria-label="Handschriftliche Unterschrift"></div>
    </div>
  </div>
</section>

<section class="page spread-right">
  <div class="room-photo" role="img" aria-label="Foto: gestalteter Wohnraum mit Kamin, Hängesessel und Holzdecke"></div>
  <div class="fact-box">
    <div class="fact-label">Daten und Fakten zum Home Staging</div>
    <div class="fact-number">75%</div>
    <p class="fact-text">In mehr als 75 Prozent aller Immobilienverkäufe mit Home Staging wurde der Angebotspreis genau erzielt oder sogar übertroffen. Dabei beträgt die Kaufpreissteigerung sogar in 40 Prozent der Fälle zwischen 5–15 % des Angebotspreises*</p>
    <p class="fact-source">* Quelle: Marktdata Home Staging, 3. Auflage März 2023</p>
  </div>
</section>

<div class="gutter"></div>

</body>
</html>
```